QR Business Card

Design a vertical orientation business card with approved logo and fonts (Jubilee Lines and Aviano). Use metallic gold and black, embossing parts of the logo.
Perhaps color back of card black?
Address:
5873 Harlow Crescent
Suite 4
Cedar Hollow FL 32817

Delia Porcaro
Managing Partner

Industry/Entity Type

Business

```html
<!DOCTYPE html>
<html lang="en">
<head>
<meta charset="utf-8">
<title>Quarry Ridge — Business Card</title>
<link rel="stylesheet" href="https://fonts.googleapis.com/css2?family=Open+Sans:ital,wght@0,400;0,600;0,700;1,400&display=swap">
<style>
  :root {
    --backdrop: #5f5f61;
    --card-white: #ffffff;
    --gold: #fcc93a;
    --ink: #111111;
    --card-black: #000000;
  }
  * { box-sizing: border-box; margin: 0; padding: 0; }
  html, body {
    width: 1200px;
    height: 796px;
    overflow: hidden;
  }
  body {
    background: var(--backdrop);
    font-family: "Open Sans", Arial, sans-serif;
    color: var(--ink);
    position: relative;
  }
  .card {
    position: absolute;
    top: 98px;
    width: 400px;
    height: 600px;
  }
  .card-front {
    left: 170px;
    background: var(--card-white);
    overflow: hidden;
  }
  .card-back {
    left: 630px;
    background: var(--card-black);
  }
  .card-shapes {
    position: absolute;
    inset: 0;
    width: 100%;
    height: 100%;
  }
  .shape-gold { fill: var(--gold); }
  .shape-black { fill: var(--card-black); }

  .brand {
    position: absolute;
    top: 118px;
    left: 0;
    width: 100%;
    text-align: center;
  }
  .brand-mark {
    display: block;
    width: 34px;
    height: 34px;
    margin: 0 auto 14px;
    background: var(--gold);
  }
  .brand-name {
    display: block;
    font-size: 27px;
    font-weight: 700;
    letter-spacing: 1.5px;
    line-height: 1.1;
    text-transform: uppercase;
  }
  .brand-sub {
    display: block;
    margin-top: 2px;
    font-size: 15px;
    font-weight: 700;
    letter-spacing: 3px;
    text-transform: uppercase;
  }

  .person {
    position: absolute;
    top: 318px;
    left: 34px;
  }
  .person-name {
    font-size: 27px;
    font-weight: 600;
    line-height: 1.1;
  }
  .person-role {
    font-size: 15px;
    font-style: italic;
    font-weight: 400;
    line-height: 1.2;
  }

  .address {
    position: absolute;
    top: 408px;
    left: 34px;
    font-style: normal;
    font-size: 19px;
    font-weight: 600;
    line-height: 1.3;
  }
</style>
</head>
<body>
  <section class="card card-front" aria-label="Business card front">
    <svg class="card-shapes" viewBox="0 0 400 600" preserveAspectRatio="none" aria-hidden="true">
      <polygon class="shape-black" points="0,0 150,0 0,330"/>
      <polygon class="shape-gold" points="150,0 400,0 400,78"/>
      <polygon class="shape-gold" points="400,112 400,548 262,600 250,600"/>
      <polygon class="shape-black" points="262,600 400,548 400,600"/>
      <polygon class="shape-black" points="0,330 16,330 0,362"/>
      <polygon class="shape-gold" points="0,362 0,600 240,600"/>
    </svg>

    <header class="brand">
      <span class="brand-mark" aria-hidden="true"></span>
      <span class="brand-name">Quarry Ridge</span>
      <span class="brand-sub">Design Studio</span>
    </header>

    <div class="person">
      <p class="person-name">Delia Porcaro</p>
      <p class="person-role">Managing Partner</p>
    </div>

    <address class="address">
      5873 Harlow Crescent<br>
      Suite 4<br>
      Cedar Hollow FL 32817
    </address>
  </section>

  <section class="card card-back" aria-label="Business card back"></section>
</body>
</html>
```